Business card design and logo needed

We have been operating as Ridgeline Paddock Fencing for 30 years but never had a logo and feel there is a need for one, but have no idea for a design.
We specialise in all types of rural fencing including post and wire, post and rail, electric, chainmesh and to a lesser extent, also do industrial security fencing.
Updates

Sorry, but website is ridgelinepaddock.net

No .au on the end!
My apologies

Regards, Barry

Target Market(s)

Rural/acreage property owners, particularly horse people.

Industry/Entity Type

Industrial

Contact Information for Business Card

Ridgeline Paddock Fencing Barry Lindqvist 0427 615302. Terry Lindqvist 0427 783160
Email: ridgelinepaddock@quolmail.com.au
Website: www.ridgelinepaddock.net.au

Requirements
Must have
• Would like to highlight website address - use the business card to advertise the website or to push them to check it out.

```html
<!DOCTYPE html>
<html lang="en">
<head>
<meta charset="utf-8">
<title>Ridgeline Paddock Fencing – Business Card</title>
<link href="https://fonts.googleapis.com/css2?family=Crimson+Pro:wght@300;400;700&display=swap" rel="stylesheet">
<style>
  :root {
    --page-bg: #ffffff;
    --card-bg: #ffffff;
    --card-edge: #231f20;
    --ink-grey: #6d6e71;
    --accent-green: #9dc43a;
    --wash-green: #ecf2d8;
    --scene-grey: #d4d5d7;
  }
  html, body {
    margin: 0;
    padding: 0;
    width: 1200px;
    height: 1000px;
    overflow: hidden;
    background: var(--page-bg);
  }
  .canvas {
    position: relative;
    width: 1200px;
    height: 1000px;
  }
  .business-card {
    position: absolute;
    left: 96px;
    top: 242px;
    width: 1026px;
    height: 577px;
    border: 1.5px solid var(--card-edge);
    background: var(--card-bg);
    overflow: hidden;
    font-family: "Crimson Pro", "Times New Roman", serif;
    color: var(--ink-grey);
  }
  .corner-wash {
    position: absolute;
    left: -174px;
    top: -95px;
    width: 526px;
    height: 526px;
    border-radius: 50%;
    background: var(--wash-green);
  }
  .contact-list {
    position: absolute;
    left: 52px;
    top: 32px;
    margin: 0;
    padding: 0;
    list-style: none;
    font-size: 32px;
    line-height: 49px;
    font-weight: 300;
  }
  .contact-list .gap { display: inline-block; width: 20px; }
  .accent { color: var(--accent-green); }
  .rural-scene {
    position: absolute;
    left: 210px;
    top: 192px;
    width: 560px;
    height: 206px;
    background: radial-gradient(ellipse at 62% 55%, var(--scene-grey) 0%, rgba(212,213,215,0.5) 50%, rgba(212,213,215,0) 72%);
  }
  .website {
    position: absolute;
    left: 0;
    right: 0;
    top: 438px;
    margin: 0;
    text-align: center;
    font-size: 72px;
    font-weight: 700;
    letter-spacing: 0.5px;
    color: var(--ink-grey);
  }
</style>
</head>
<body>
<div class="canvas">
  <section class="business-card" aria-label="Ridgeline Paddock Fencing business card">
    <div class="corner-wash"></div>
    <ul class="contact-list">
      <li>Barry Lindqvist 0427 615302</li>
      <li>Terry Lindqvist<span class="gap"></span>0427 783160</li>
      <li><span class="accent">E</span>mail: ridgelinepaddock@quolmail.com.au</li>
    </ul>
    <div class="rural-scene" role="img" aria-label="Grey illustration of a farm shed with a horse walking beside a two-strand barbed wire fence"></div>
    <p class="website">www.<span class="accent">r</span>idgeline<span class="accent">p</span>addock.net</p>
  </section>
</div>
</body>
</html>
```